TRV Capability Statement Brochure

We need a four or six-page flyer/brochure for our capability statement. This should include all the key written copy and photos/descriptions of the personnel, plus contact addresses in the current capability statement which is attached. We are looking for a modern, professional design that matches our professional approach to our business. Please incorporate our logo into the design.

Target Market(s)

Government departments, shipping companies, port operators, lawyers, export and import businesses, commodity companies.

Industry/Entity Type

Business Consultant

Contact Information for Business Card

Professional, simple to read, uncomplicated.

Font styles to use
Serif
Sans Serif

Colors

Designer to choose colors to be used in the design.

Requirements
Must have
• Company logo
• KEY MESSAGE: Providing independent, expert, confidential and professional services.
• Description of company
• Description and photos of personnel.
• Contact details.
Should not have
• No cliches

```html
<!DOCTYPE html>
<html lang="en">
<head>
<meta charset="utf-8">
<title>TRV Capability Statement 2017 – Cover</title>
<link href="https://fonts.googleapis.com/css2?family=Arimo:wght@400;700&display=swap" rel="stylesheet">
<style>
  :root {
    --backdrop: #c9cacb;
    --navy: #15203d;
    --navy-deep: #101a33;
    --band-blue: #2b4a8a;
    --edge-blue: #3c5f9e;
    --headline: #c9cdd7;
    --caption: #bfc4cf;
    --logo: #ffffff;
  }
  * { margin: 0; padding: 0; box-sizing: border-box; }
  html, body {
    width: 1200px;
    height: 928px;
    overflow: hidden;
    background: var(--backdrop);
    font-family: "Arimo", Arial, sans-serif;
  }
  .canvas {
    position: relative;
    width: 1200px;
    height: 928px;
  }
  .cover {
    position: absolute;
    left: 296px;
    top: 34px;
    width: 608px;
    height: 860px;
    background: var(--navy);
    overflow: hidden;
    box-shadow: 0 6px 18px rgba(0, 0, 0, 0.25);
  }
  .cover-art {
    position: absolute;
    inset: 0;
    width: 100%;
    height: 100%;
  }
  .brand {
    position: absolute;
    left: 64px;
    top: 118px;
    color: var(--logo);
  }
  .brand-name {
    font-weight: 700;
    font-size: 36px;
    letter-spacing: 1px;
    line-height: 1;
  }
  .brand-tagline {
    margin-top: 4px;
    font-weight: 400;
    font-size: 7px;
    letter-spacing: 1.2px;
    color: var(--caption);
  }
  .key-message {
    position: absolute;
    left: 72px;
    top: 210px;
    width: 330px;
    font-weight: 700;
    font-size: 22px;
    line-height: 1.22;
    color: var(--headline);
  }
  .document-title {
    position: absolute;
    left: 100px;
    top: 380px;
    font-size: 11px;
    color: var(--caption);
  }
</style>
</head>
<body>
<div class="canvas">
  <section class="cover">
    <svg class="cover-art" viewBox="0 0 608 860" preserveAspectRatio="none">
      <defs>
        <linearGradient id="seaTone" x1="0" y1="0" x2="0" y2="1">
          <stop offset="0" stop-color="#b7b0a6"/>
          <stop offset="0.25" stop-color="#8d93a0"/>
          <stop offset="0.55" stop-color="#4d6680"/>
          <stop offset="1" stop-color="#1f3650"/>
        </linearGradient>
        <radialGradient id="sunGlare" cx="0.75" cy="0.3" r="0.45">
          <stop offset="0" stop-color="#f2e6d2" stop-opacity="0.85"/>
          <stop offset="1" stop-color="#f2e6d2" stop-opacity="0"/>
        </radialGradient>
      </defs>
      <g role="img" aria-label="Aerial photograph of cargo ships on a sunlit sea">
        <path d="M430 0 C300 220 232 520 252 860 L608 860 L608 0 Z" fill="url(#seaTone)"/>
        <path d="M430 0 C300 220 232 520 252 860 L608 860 L608 0 Z" fill="url(#sunGlare)"/>
      </g>
      <path class="photo-edge" d="M412 0 C282 220 214 520 234 860" fill="none" stroke="var(--edge-blue)" stroke-width="2"/>
      <path class="corner-band" d="M330 860 C430 770 520 705 608 648 L608 860 Z" fill="var(--band-blue)"/>
    </svg>

    <div class="brand">
      <div class="brand-name">TRV</div>
      <div class="brand-tagline">MARITIME ADVISORY GROUP</div>
    </div>

    <h1 class="key-message">Providing independent, expert, confidential and professional services</h1>

    <p class="document-title">Capability Statement 2017</p>
  </section>
</div>
</body>
</html>
```